We want a business card/punch card for our business. We are including examples of our current business card (we like the front of our business card and not looking to remake it). We need only back side to be designed in form of a punch card (we are including a sample of the punch card we made, but are unsatisfied). For each $180 spend (9 punches) our clients have $20 off.

Colors
886aae

```html
<!DOCTYPE html>
<html lang="en">
<head>
<meta charset="utf-8">
<title>Lumen Practices – Business Card &amp; Punch Card</title>
<link href="https://fonts.googleapis.com/css2?family=Cinzel:wght@400;600&family=EB+Garamond:wght@400;600&family=Lato:wght@300;400&display=swap" rel="stylesheet">
<style>
  :root {
    --backdrop: #2d2d2d;
    --card: #050505;
    --brand-blue: #5b67c2;
    --brand-purple: #6a2fa0;
    --lavender: #886aae;
    --text-light: #ececec;
    --punch-frame: #4a4234;
  }
  * { box-sizing: border-box; margin: 0; padding: 0; }
  html, body { width: 1200px; height: 1200px; overflow: hidden; background: var(--backdrop); }
  .card {
    position: absolute; left: 223px; width: 815px; height: 466px;
    background: var(--card);
  }
  .card--front { top: 76px; background: radial-gradient(ellipse at 50% 30%, #141414 0%, #050505 70%); }
  .card--back { top: 658px; }

  .brand-name {
    position: absolute; color: var(--brand-blue);
    font-family: "EB Garamond", serif; font-weight: 600; text-align: center; line-height: 0.95;
  }
  .card--front .brand-name { left: 60px; top: 150px; width: 300px; font-size: 62px; }
  .card--back .brand-name { left: 0; top: 38px; width: 815px; font-size: 96px; line-height: 1.2; }
  .brand-dot {
    display: inline-block; width: 0.22em; height: 0.22em; border-radius: 50%;
    background: var(--brand-blue); vertical-align: middle; margin-left: 0.12em;
  }

  .holder-name {
    position: absolute; left: 426px; top: 156px;
    font-family: "Cinzel", serif; font-size: 30px; color: var(--brand-blue); letter-spacing: 0.5px;
  }
  .contact-list { position: absolute; left: 433px; top: 192px; list-style: none; }
  .contact-item {
    display: flex; align-items: center; height: 26px;
    font-family: "EB Garamond", serif; font-size: 21px; color: var(--text-light);
  }
  .contact-icon { width: 14px; height: 14px; margin-right: 10px; flex: none; }

  .service-list {
    position: absolute; left: 0; top: 186px; width: 815px;
    font-family: "Lato", sans-serif; font-weight: 300; font-size: 26px; color: var(--text-light);
    text-align: center;
  }
  .service-line { height: 36px; line-height: 34px; white-space: nowrap; }
  .service-line--rule-below { display: inline-block; border-bottom: 2px solid var(--brand-purple); padding: 0 4px; }
  .bullet {
    display: inline-block; width: 13px; height: 13px; border-radius: 50%;
    background: var(--brand-blue); margin: 0 8px; vertical-align: middle;
  }

  .punch-row {
    position: absolute; left: 30px; top: 354px; width: 760px;
    display: flex; justify-content: space-between;
  }
  .punch {
    width: 80px; height: 80px; border-radius: 50%; background: var(--punch-frame);
    display: flex; align-items: center; justify-content: center;
  }
  .punch-value {
    width: 50px; height: 50px; border-radius: 50%; background: var(--brand-blue);
    border: 2px solid #d9d2c0;
    display: flex; align-items: center; justify-content: center;
    font-family: "Lato", sans-serif; font-size: 15px; color: #fff;
  }
</style>
</head>
<body>

<section class="card card--front">
  <div class="brand-name">Lumen<br>Practices<span class="brand-dot"></span></div>

  <div class="holder-name">SELENA MARLOWE</div>
  <ul class="contact-list">
    <li class="contact-item">
      <svg class="contact-icon" viewBox="0 0 16 16"><path d="M3 1l3 3-2 2c1 2 3 4 5 5l2-2 3 3-2 3C7 15 1 9 0 4z" fill="var(--brand-blue)"/></svg>
      +(555) -014- 2290
    </li>
    <li class="contact-item">
      <svg class="contact-icon" viewBox="0 0 16 16"><rect x="0" y="3" width="16" height="11" fill="var(--brand-blue)"/><path d="M0 3l8 6 8-6" stroke="#050505" stroke-width="1.5" fill="none"/></svg>
      hello@lumenpractices.com
    </li>
    <li class="contact-item">
      <svg class="contact-icon" viewBox="0 0 16 16" fill="none" stroke="var(--brand-blue)" stroke-width="1.3"><circle cx="8" cy="8" r="7"/><ellipse cx="8" cy="8" rx="3" ry="7"/><path d="M1 8h14M2 4.5h12M2 11.5h12"/></svg>
      www.lumenpractices.com
    </li>
    <li class="contact-item">
      <svg class="contact-icon" viewBox="0 0 16 16"><rect x="1" y="1" width="14" height="14" rx="2" fill="var(--brand-blue)"/></svg>
      social.lumenpractices.com/page
    </li>
    <li class="contact-item">
      <svg class="contact-icon" viewBox="0 0 16 16"><circle cx="8" cy="8" r="7" fill="var(--brand-blue)"/></svg>
      groups.lumenpractices.com/circle
    </li>
  </ul>
</section>

<section class="card card--back">
  <div class="brand-name">Lumen Practices<span class="brand-dot"></span></div>

  <div class="service-list">
    <div class="service-line"><span class="service-line--rule-below">Tantra<span class="bullet"></span>Tao<span class="bullet"></span>Yaga<span class="bullet"></span>Tai Chi<span class="bullet"></span>Reiki</span></div>
    <div class="service-line">Sacred Sexuality<span class="bullet"></span>Sexual Healing<span class="bullet"></span>Sound Healing</div>
    <div class="service-line"><span class="service-line--rule-below">Energy Work<span class="bullet"></span>Rituals</span></div>
    <div class="service-line">Partners Yoga<span class="bullet"></span>Four Hand Massage</div>
  </div>

  <div class="punch-row">
    <div class="punch" role="img" aria-label="ornamental mandala punch frame"><span class="punch-value">180$</span></div>
    <div class="punch" role="img" aria-label="ornamental mandala punch frame"><span class="punch-value">180$</span></div>
    <div class="punch" role="img" aria-label="ornamental mandala punch frame"><span class="punch-value">180$</span></div>
    <div class="punch" role="img" aria-label="ornamental mandala punch frame"><span class="punch-value">180$</span></div>
    <div class="punch" role="img" aria-label="ornamental mandala punch frame"><span class="punch-value">180$</span></div>
    <div class="punch" role="img" aria-label="ornamental mandala punch frame"><span class="punch-value">180$</span></div>
    <div class="punch" role="img" aria-label="ornamental mandala punch frame"><span class="punch-value">180$</span></div>
    <div class="punch" role="img" aria-label="ornamental mandala punch frame"><span class="punch-value">180$</span></div>
    <div class="punch" role="img" aria-label="ornamental mandala punch frame"><span class="punch-value">180$</span></div>
  </div>
</section>

</body>
</html>
```